Managed Service Provider need new business cards

We are a small Maanged Service Provider of IT Services and need a new fresh design for our business cards. We want something impossible, fun and professional :)
Our services has a large range, but we are always fun and make sure our customers both get their issue sorted and also feel like they are "catching up with an old friend".
All our cards in the past has always been all black, with red and we need something fresher.
The back of card, we would like just a small list of what we do i think, but if someone has a better idea, please do something cool with the back of the card:
Managed IT Services
Productivity Solutions
Data Backup and Recovery
IT System Maintenance
Managed IT Security
More details can be found on our website tqnetworks.com.au
Industry/Entity Type
It Company
Contact Information for Business Card
Name: Dwayne Falstrup
Title: Director
Phone: 03 6193 4827
Mobile: 0412 587 239
Email: dwayne@tqnetworks.com.au
Web: www.tqnetworks.com.au

```html
<!DOCTYPE html>
<html lang="en">
<head>
<meta charset="utf-8">
<title>TQ Networks – Business Card</title>
<link rel="stylesheet" href="https://fonts.googleapis.com/css2?family=Lato:wght@400;700;900&display=swap">
<style>
  :root {
    --red: #e3202a;
    --red-soft: #ef4a52;
    --ink: #3a3a3a;
    --grey: #6b6b6b;
    --paper: #ffffff;
    --black: #0d0d0f;
    --black-hi: #2a2a2e;
    --backdrop: #ecebe8;
  }
  * { margin: 0; padding: 0; box-sizing: border-box; }
  html, body {
    width: 1200px; height: 913px; overflow: hidden;
    background: var(--backdrop);
    font-family: "Lato", sans-serif;
  }
  .canvas { position: relative; width: 1200px; height: 913px; }

  .card {
    position: absolute;
    width: 600px; height: 367px;
    border-radius: 4px;
    box-shadow: 0 14px 30px rgba(0,0,0,.18), 0 3px 0 var(--red);
    overflow: hidden;
  }
  .card-front { left: 80px; top: 60px; background: var(--paper); }
  .card-back {
    left: 520px; top: 480px;
    background: linear-gradient(135deg, var(--black-hi) 0%, var(--black) 45%, #000 100%);
  }

  .brand {
    position: absolute;
    left: 40px; top: 172px;
    width: 256px;
    display: flex; align-items: center; gap: 10px;
    white-space: nowrap;
  }
  .brand-dot {
    width: 18px; height: 18px; border-radius: 50%;
    background: var(--red); flex: none;
  }
  .brand-name {
    font-weight: 900; font-size: 26px; letter-spacing: 0.5px;
    color: var(--red); text-transform: uppercase; line-height: 1;
  }

  .divider {
    position: absolute; left: 318px; top: 95px;
    width: 1px; height: 180px; background: var(--red-soft);
  }

  .contact { position: absolute; left: 348px; top: 98px; }
  .person-name { font-size: 30px; font-weight: 700; color: var(--red); line-height: 1.1; white-space: nowrap; }
  .person-title { font-size: 17px; color: var(--grey); margin: 4px 0 16px; }
  .contact-list { list-style: none; }
  .contact-list li {
    display: flex; align-items: center; gap: 12px;
    font-size: 15px; color: var(--ink); line-height: 26px; white-space: nowrap;
  }
  .contact-list svg { width: 15px; height: 15px; fill: var(--red); flex: none; }
  .contact-list .accent { color: var(--red); }

  .services {
    position: absolute; left: 348px; top: 108px; list-style: none;
  }
  .services li {
    position: relative; padding-left: 22px;
    font-size: 17px; line-height: 31px; color: #f2f2f2; white-space: nowrap;
  }
  .services li::before {
    content: ""; position: absolute; left: 0; top: 13px;
    width: 7px; height: 7px; border-radius: 50%; background: var(--red);
  }
</style>
</head>
<body>
<main class="canvas">

  <section class="card card-front" aria-label="Business card front">
    <div class="brand">
      <span class="brand-dot"></span>
      <span class="brand-name">TQ Networks</span>
    </div>
    <div class="divider"></div>
    <div class="contact">
      <h1 class="person-name">Dwayne Falstrup</h1>
      <p class="person-title">Director</p>
      <ul class="contact-list">
        <li>
          <svg viewBox="0 0 24 24" aria-hidden="true"><path d="M6.6 10.8a15 15 0 0 0 6.6 6.6l2.2-2.2c.3-.3.7-.4 1-.2 1.1.4 2.3.6 3.6.6.6 0 1 .4 1 1V20c0 .6-.4 1-1 1A17 17 0 0 1 3 4c0-.6.4-1 1-1h3.5c.6 0 1 .4 1 1 0 1.3.2 2.5.6 3.6.1.3 0 .7-.2 1z"/></svg>
          03 6193 4827
        </li>
        <li>
          <svg viewBox="0 0 24 24" aria-hidden="true"><path d="M7 1h10a2 2 0 0 1 2 2v18a2 2 0 0 1-2 2H7a2 2 0 0 1-2-2V3a2 2 0 0 1 2-2zm0 3v14h10V4zm5 15.5a1 1 0 1 0 0 2 1 1 0 0 0 0-2z"/></svg>
          0412 587 239
        </li>
        <li>
          <svg viewBox="0 0 24 24" aria-hidden="true"><path d="M2 5h20v14H2zm2 2v.5l8 5.5 8-5.5V7zm0 3v7h16v-7l-8 5.5z"/></svg>
          dwayne@tqnetworks.com.au
        </li>
        <li>
          <svg viewBox="0 0 24 24" aria-hidden="true"><path d="M12 2a10 10 0 1 0 0 20 10 10 0 0 0 0-20zm6.9 9h-3a15 15 0 0 0-1.3-5.6A8 8 0 0 1 18.9 11zM12 4c.9 1.2 1.8 3.6 1.9 7h-3.8C10.2 7.6 11.1 5.2 12 4zM9.4 5.4A15 15 0 0 0 8.1 11h-3a8 8 0 0 1 4.3-5.6zM5.1 13h3a15 15 0 0 0 1.3 5.6A8 8 0 0 1 5.1 13zm6.9 7c-.9-1.2-1.8-3.6-1.9-7h3.8c-.1 3.4-1 5.8-1.9 7zm2.6-1.4a15 15 0 0 0 1.3-5.6h3a8 8 0 0 1-4.3 5.6z"/></svg>
          <span>www.<span class="accent">tqnetworks</span>.com.au</span>
        </li>
      </ul>
    </div>
  </section>

  <section class="card card-back" aria-label="Business card back">
    <div class="brand">
      <span class="brand-dot"></span>
      <span class="brand-name">TQ Networks</span>
    </div>
    <div class="divider"></div>
    <ul class="services">
      <li>Managed IT Services</li>
      <li>Productivity Solutions</li>
      <li>Data Backup and Recovery</li>
      <li>IT System Maintenance</li>
      <li>Managed IT Security</li>
    </ul>
  </section>

</main>
</body>
</html>
```